Ironbark & Vale Construction and Developments business cards

A business card with watermark background (construction work)

Home improvement projects
House renovations
Bathroom and kitchen renovations
House extensions
New builds and granny flats

Director Tomas Verhoeven
(Phone number)
tomas@ivkbuilds.com.au
(Instagram logo) ivk_builds

```html
<!DOCTYPE html>
<html lang="en">
<head>
<meta charset="utf-8">
<title>Ironbark &amp; Vale Construction and Developments – Business Cards</title>
<link rel="stylesheet" href="https://fonts.googleapis.com/css2?family=Montserrat:wght@500;600;700&display=swap">
<style>
  :root {
    --backdrop: #454547;
    --brand-blue: #3a78b4;
    --brand-blue-deep: #1f5fae;
    --photo-light: #2f7fc6;
    --photo-dark: #2a3f9a;
    --card-white: #ffffff;
    --ink-grey: #3f4043;
    --text-white: #ffffff;
  }
  * { box-sizing: border-box; margin: 0; padding: 0; }
  html, body {
    width: 1200px; height: 1200px; overflow: hidden;
    background: var(--backdrop);
    font-family: "Montserrat", sans-serif;
  }
  .sheet { position: relative; width: 1200px; height: 1200px; }

  .card {
    position: absolute; left: 181px;
    width: 838px; height: 478px;
    border-radius: 30px; overflow: hidden;
  }

  /* Back side */
  .card--back { top: 90px; color: var(--text-white); }
  .card__photo {
    position: absolute; inset: 0;
    background: linear-gradient(160deg, var(--photo-light) 0%, #2a6dbd 45%, var(--photo-dark) 100%);
  }
  .services { position: absolute; left: 64px; top: 54px; }
  .services__title { font-size: 38px; font-weight: 700; letter-spacing: 0.5px; margin-bottom: 10px; }
  .services__list { list-style: none; font-size: 22px; font-weight: 600; line-height: 28px; }
  .services__list li::before { content: "·"; margin-right: 10px; }
  .back-wordmark {
    position: absolute; left: 64px; bottom: 48px;
    font-weight: 600; color: var(--text-white); line-height: 1.05;
  }
  .back-wordmark__main { font-size: 38px; display: block; }
  .back-wordmark__sub { font-size: 26px; display: block; margin-top: 2px; }
  .back-wordmark__tail { font-size: 13px; letter-spacing: 9px; text-transform: uppercase; display: block; margin-top: 6px; }

  /* Front side */
  .card--front { top: 620px; background: var(--card-white); }
  .name-band {
    position: absolute; left: 0; top: 196px;
    width: 412px; height: 94px;
    background: var(--brand-blue);
    border-radius: 0 6px 6px 0;
    color: var(--text-white);
  }
  .name-band__name {
    position: absolute; left: 38px; top: 8px;
    font-size: 34px; font-weight: 700; letter-spacing: -0.5px;
    line-height: 1.2; white-space: nowrap;
  }
  .name-band__role { position: absolute; left: 40px; top: 56px; font-size: 21px; font-weight: 500; line-height: 1.2; white-space: nowrap; }

  .brand {
    position: absolute; left: 460px; top: 70px; width: 330px;
    text-align: center; color: var(--brand-blue); font-weight: 600;
  }
  .brand__mark { width: 54px; height: 54px; background: var(--brand-blue); margin: 0 auto 16px; border-radius: 4px; }
  .brand__name { font-size: 31px; line-height: 1.1; display: block; white-space: nowrap; }
  .brand__sub { font-size: 24px; display: block; margin-top: 2px; }
  .brand__tail { font-size: 11px; letter-spacing: 8px; text-transform: uppercase; display: block; margin-top: 4px; }
  .brand__tagline {
    display: inline-block; margin-top: 12px; padding: 0 6px 2px;
    font-size: 19px; color: var(--brand-blue);
    border-bottom: 2px solid var(--brand-blue);
  }

  .contacts { position: absolute; left: 38px; top: 332px; list-style: none; }
  .contacts li {
    display: flex; align-items: center; gap: 11px;
    font-size: 24px; font-weight: 600; color: var(--brand-blue);
    height: 32px; white-space: nowrap;
  }
  .contacts svg { width: 22px; height: 22px; flex: none; }

  .social { position: absolute; left: 487px; top: 364px; color: var(--brand-blue); font-weight: 600; white-space: nowrap; }
  .social__label { font-size: 23px; display: block; margin-bottom: 8px; }
  .social__handle { display: flex; align-items: center; gap: 10px; font-size: 24px; }
  .social__dot { width: 28px; height: 28px; border-radius: 50%; border: 3px solid var(--ink-grey); }
</style>
</head>
<body>
<main class="sheet">

  <section class="card card--back">
    <div class="card__photo" role="img" aria-label="Blue-toned watermark photo of builders working on a timber roof frame at a construction site"></div>
    <div class="services">
      <h2 class="services__title">Services We Offer:</h2>
      <ul class="services__list">
        <li>Home improvement projects</li>
        <li>House renovations</li>
        <li>Bathroom and kitchen</li>
        <li>Renovations</li>
        <li>House extensions</li>
        <li>New builds and granny flats</li>
      </ul>
    </div>
    <p class="back-wordmark">
      <span class="back-wordmark__main">Ironbark &amp; Vale</span>
      <span class="back-wordmark__sub">Construction</span>
      <span class="back-wordmark__tail">and Developments</span>
    </p>
  </section>

  <section class="card card--front">
    <div class="name-band">
      <h1 class="name-band__name">Tomas Verhoeven</h1>
      <p class="name-band__role">DIRECTOR</p>
    </div>

    <div class="brand">
      <div class="brand__mark"></div>
      <span class="brand__name">Ironbark &amp; Vale</span>
      <span class="brand__sub">Construction</span>
      <span class="brand__tail">and Developments</span>
      <span class="brand__tagline">Built right, every time!</span>
    </div>

    <ul class="contacts">
      <li>
        <svg viewBox="0 0 24 24" aria-hidden="true"><circle cx="12" cy="12" r="11" fill="#3f4043"/><path d="M8.2 6.5l2 2.2-1.2 1.6c.8 1.7 2 2.9 3.7 3.7l1.6-1.2 2.2 2-1.1 1.9c-3.9-.3-8.2-4.6-8.5-8.5z" fill="#fff"/></svg>
        215 000 7391
      </li>
      <li>
        <svg viewBox="0 0 24 24" aria-hidden="true"><rect x="1.5" y="5" width="21" height="14" fill="none" stroke="#3f4043" stroke-width="2"/><path d="M1.5 5l10.5 8 10.5-8M1.5 19l8-7M22.5 19l-8-7" fill="none" stroke="#3f4043" stroke-width="2"/></svg>
        tomas@ivkbuilds.com.au
      </li>
      <li>
        <svg viewBox="0 0 24 24" aria-hidden="true"><circle cx="12" cy="12" r="10" fill="none" stroke="#3f4043" stroke-width="2"/><ellipse cx="12" cy="12" rx="4.5" ry="10" fill="none" stroke="#3f4043" stroke-width="1.6"/><path d="M2 12h20M4 7h16M4 17h16" stroke="#3f4043" stroke-width="1.6"/></svg>
        ivkbuilds.com.au
      </li>
    </ul>

    <div class="social">
      <span class="social__label">Find us on social</span>
      <span class="social__handle"><span class="social__dot"></span>ivk_builds</span>
    </div>
  </section>

</main>
</body>
</html>
```